Lawn mowing business card design

We need a business card design for our lawn mowing and gardening business which is located in the Northern Beaches of Sydney. Our business name is Meadowline Turf and our logo is predominantly green and yellow in color. Please see our website at www.meadowlineturf.com.au for design ideas. The business targets young professionals and older clientele. As such the font should be easy to read, but I also want the business card to be colorful and stand out.

Target Market(s)

young professionals

Industry/Entity Type

Lawn Care

Contact Information for Business Card

Meadowline Turf, Gareth Pellow, 0478559201, www.meadowlineturf.com.au, email: meadowlineturf@mailbox-example.com

Font styles to use
Serif

Colors
9bcb3b
fbed22

Requirements
Must have
• Must include the details listed above. Must include the attached logo.
Nice to have
• Logo attached with two copies. The logo without any writing is high quality, please feel free to be creative with the text stating our business name "Meadowline Turf" using this file.

```html
<!DOCTYPE html>
<html lang="en">
<head>
<meta charset="utf-8">
<title>Meadowline Turf – Business Card</title>
<link rel="stylesheet" href="https://fonts.googleapis.com/css2?family=Open+Sans:wght@400;600;700&display=swap">
<style>
  :root {
    --bg: #ecebe6;
    --card-white: #ffffff;
    --card-shade: #eeeeee;
    --green: #9bcb3b;
    --green-light: #c4e35a;
    --green-deep: #6fb52c;
    --yellow: #fbed22;
    --ink: #3a3a3a;
    --ink-soft: #555555;
    --divider: #d8e86a;
  }
  * { box-sizing: border-box; margin: 0; padding: 0; }
  html, body {
    width: 1200px; height: 1062px; overflow: hidden;
    background: var(--bg);
    font-family: "Open Sans", Arial, sans-serif;
  }
  .canvas { position: relative; width: 1200px; height: 1062px; }

  .card {
    position: absolute;
    width: 700px; height: 400px;
    border-radius: 4px;
    box-shadow: 0 8px 22px rgba(0,0,0,.18);
    overflow: hidden;
  }

  /* Front side */
  .card-front {
    left: 70px; top: 70px;
    background: linear-gradient(160deg, var(--card-white) 40%, var(--card-shade) 100%);
  }
  .card-front .band {
    position: absolute; left: 0; right: 0; bottom: 0; height: 60px;
    background: linear-gradient(180deg, var(--green-light), var(--green-deep));
  }
  .front-brand {
    position: absolute; left: 50px; top: 150px;
    display: flex; align-items: center; gap: 12px;
  }
  .brand-dot {
    width: 34px; height: 34px; border-radius: 50%;
    background: var(--yellow);
  }
  .brand-name {
    font-weight: 600; font-size: 24px; color: var(--ink);
  }
  .divider {
    position: absolute; left: 340px; top: 70px;
    width: 1px; height: 210px;
    background: var(--divider);
  }
  .details {
    position: absolute; left: 375px; top: 56px;
    color: var(--ink-soft);
  }
  .person-name {
    font-weight: 700; font-size: 26px; color: var(--green);
    line-height: 1.1;
  }
  .person-role { font-size: 16px; margin-top: 2px; }
  .address { font-size: 15px; line-height: 1.45; margin-top: 26px; }
  .contact-list { list-style: none; margin-top: 22px; font-size: 14.5px; line-height: 1.75; }
  .contact-list li { display: flex; align-items: center; gap: 10px; }
  .contact-list svg { width: 14px; height: 14px; flex: none; }

  /* Back side */
  .card-back {
    left: 430px; top: 590px;
    background: radial-gradient(circle at 70% 25%, var(--green-light) 0%, var(--green) 55%, var(--green-deep) 100%);
  }
  .back-brand {
    position: absolute; inset: 0;
    display: flex; align-items: center; justify-content: center; gap: 20px;
  }
  .back-brand .brand-dot { width: 64px; height: 64px; }
  .back-brand .brand-name { font-size: 46px; color: #2f2f2f; }
</style>
</head>
<body>
<main class="canvas">

  <section class="card card-front" aria-label="Business card front">
    <div class="front-brand">
      <span class="brand-dot"></span>
      <span class="brand-name">Meadowline Turf</span>
    </div>
    <div class="divider"></div>
    <div class="details">
      <p class="person-name">Gareth Pellow</p>
      <p class="person-role">Manager</p>
      <p class="address">Unit 48 Harbour Lane 7<br>Block 9, Collaroy</p>
      <ul class="contact-list">
        <li>
          <svg viewBox="0 0 14 14" aria-hidden="true"><path d="M3 1l2.5 3-1.3 1.3c.8 1.8 2 3 3.8 3.8L9.3 7.8l3 2.5-1.6 2.2C6 12 2 8 1.5 3.2z" fill="#9bcb3b"/></svg>
          0478559201
        </li>
        <li>
          <svg viewBox="0 0 14 14" aria-hidden="true"><g fill="none" stroke="#9bcb3b" stroke-width="1.2"><circle cx="7" cy="7" r="5.8"/><ellipse cx="7" cy="7" rx="2.6" ry="5.8"/><path d="M1.2 7h11.6"/></g></svg>
          www.meadowlineturf.com.au
        </li>
        <li>
          <svg viewBox="0 0 14 14" aria-hidden="true"><g fill="none" stroke="#9bcb3b" stroke-width="1.4"><circle cx="7" cy="7" r="2.4"/><path d="M9.4 5v3.2c0 1.6 2.9 1.6 2.9-1.2A5.6 5.6 0 1 0 9.8 12"/></g></svg>
          meadowlineturf@mailbox-example.com
        </li>
      </ul>
    </div>
    <div class="band"></div>
  </section>

  <section class="card card-back" aria-label="Business card back">
    <div class="back-brand">
      <span class="brand-dot"></span>
      <span class="brand-name">Meadowline Turf</span>
    </div>
  </section>

</main>
</body>
</html>
```